Business Card Design Project

I have attached the logo and the colour pallete for the branding for the company.

Creative designs for business cards are needed.

The Company is modern corporate.

Industry/Entity Type

Business

```html
<!DOCTYPE html>
<html lang="en">
<head>
<meta charset="utf-8">
<title>Knowhub Business Card</title>
<link href="https://fonts.googleapis.com/css2?family=Lato:wght@400;700&display=swap" rel="stylesheet">
<style>
  :root {
    --page-bg: #efece8;
    --purple-edge: #3e1545;
    --purple-mid: #6d2668;
    --orange-top: #f7941d;
    --orange-bottom: #f15a24;
    --ink: #ffffff;
    --shadow: rgba(0, 0, 0, 0.35);
  }
  * { margin: 0; padding: 0; box-sizing: border-box; }
  html, body {
    width: 1200px;
    height: 1000px;
    overflow: hidden;
    background: var(--page-bg);
    font-family: "Lato", sans-serif;
    color: var(--ink);
  }
  .card {
    position: absolute;
    top: 350px;
    width: 535px;
    height: 300px;
    background: linear-gradient(90deg, var(--purple-edge) 0%, var(--purple-mid) 50%, var(--purple-edge) 100%);
    box-shadow: 3px 5px 10px var(--shadow);
    overflow: hidden;
  }
  .card--front { left: 47px; }
  .card--back { left: 618px; }
  .accent-bar {
    position: absolute;
    top: 0;
    width: 13px;
    height: 100%;
    background: linear-gradient(180deg, var(--orange-top), var(--orange-bottom));
  }
  .card--front .accent-bar { left: 0; }
  .card--back .accent-bar { right: 0; }

  .contact-list {
    position: absolute;
    left: 35px;
    top: 23px;
    list-style: none;
  }
  .contact-list li {
    display: flex;
    align-items: center;
    height: 22.5px;
    font-size: 13px;
  }
  .contact-list svg {
    width: 17px;
    height: 17px;
    margin-right: 11px;
    flex: none;
  }
  .holder {
    position: absolute;
    right: 25px;
    bottom: 20px;
    text-align: right;
    font-size: 24px;
    line-height: 1.3;
  }
  .holder .role { padding-right: 24px; }

  .tagline {
    position: absolute;
    left: 25px;
    top: 22px;
    font-size: 12px;
    line-height: 1.3;
  }
  .brand-name {
    position: absolute;
    right: 35px;
    bottom: 22px;
    font-size: 30px;
    font-weight: 700;
    letter-spacing: -0.5px;
  }
</style>
</head>
<body>
  <section class="card card--front">
    <div class="accent-bar"></div>
    <ul class="contact-list">
      <li>
        <svg viewBox="0 0 20 20"><circle cx="10" cy="10" r="9" fill="none" stroke="#fff" stroke-width="1.5"/><path d="M6.5 5.5l2 0 .8 2.5-1.2 1a6 6 0 0 0 3 3l1-1.2 2.5.8v2a1 1 0 0 1-1 1A8 8 0 0 1 5.5 6.5a1 1 0 0 1 1-1z" fill="#fff"/></svg>
        0140 220 318
      </li>
      <li>
        <svg viewBox="0 0 20 20"><circle cx="10" cy="10" r="9" fill="none" stroke="#fff" stroke-width="1.5"/><rect x="7" y="4.5" width="6" height="11" rx="1" fill="none" stroke="#fff" stroke-width="1.4"/><circle cx="10" cy="13.3" r="0.8" fill="#fff"/></svg>
        0955 781 604
      </li>
      <li>
        <svg viewBox="0 0 20 20"><circle cx="10" cy="10" r="9" fill="none" stroke="#fff" stroke-width="1.5"/><text x="10" y="14" text-anchor="middle" font-family="Lato, sans-serif" font-size="11" font-weight="700" fill="#fff">@</text></svg>
        office@knowhub.com
      </li>
      <li>
        <svg viewBox="0 0 20 20"><circle cx="10" cy="10" r="9" fill="none" stroke="#fff" stroke-width="1.5"/><ellipse cx="10" cy="10" rx="3.5" ry="8.5" fill="none" stroke="#fff" stroke-width="1.2"/><path d="M2 10h16M3.5 6h13M3.5 14h13" stroke="#fff" stroke-width="1.2"/></svg>
        www.knowhub.com
      </li>
      <li>
        <svg viewBox="0 0 20 20"><circle cx="10" cy="10" r="6" fill="#fff"/></svg>
        /knowhub
      </li>
      <li>
        <svg viewBox="0 0 20 20"><circle cx="10" cy="10" r="6" fill="#fff"/></svg>
        @knowhub
      </li>
    </ul>
    <div class="holder">
      <div class="name">Sam Carter</div>
      <div class="role">CEO</div>
    </div>
  </section>

  <section class="card card--back">
    <div class="accent-bar"></div>
    <p class="tagline">1st online information<br>resource centre for all<br>of your 'how to' questions</p>
    <div class="brand-name">knowhub</div>
  </section>
</body>
</html>
```